Etiketten-Design für Trinkweine
Zielgruppe
Wir sind eine Weinkellerei, die einfache Trinkweine für den LEH herstellt.
Unsere Zielgruppen sind Jugendliche .
Wir suchen ein Etikett für unser neues Produkt ,,Traubensaftschorle`` alkoholfrei
Aufgabenstellung
Siehe Anhang , eigene ideen sind auch erwünscht.
Das Etikett sollte Natur verbunden wirken da es ein Bio Produkt ist.
Farben: weiß, grün wären erwünscht.
Das Etikett sollte 75mm hoch und 120mm Breit sein
Strukturpapier weiß
Anbei auch unserer Standartetikett gerne kann das Logo übernommen werden

```html
<!DOCTYPE html>
<html lang="de">
<head>
<meta charset="utf-8">
<title>Traubensaftschorle – Etikett</title>
<link rel="stylesheet" href="https://fonts.googleapis.com/css2?family=Archivo:wght@500;800&display=swap">
<style>
  :root {
    --backdrop: #f2f2f2;
    --label: #ffffff;
    --label-edge: #c9c9c9;
    --ink: #333333;
    --green-light: #8fdc5a;
    --green-dark: #3fc24a;
  }
  html, body {
    margin: 0;
    width: 818px;
    height: 1200px;
    overflow: hidden;
    background: var(--backdrop);
  }
  .label {
    position: absolute;
    left: 55px;
    top: 39px;
    width: 708px;
    height: 1122px;
    background: var(--label);
    border: 2px solid var(--label-edge);
    box-sizing: border-box;
    font-family: "Archivo", Arial, sans-serif;
    color: var(--ink);
    overflow: hidden;
  }
  .winery {
    position: absolute;
    top: 28px;
    left: 0;
    width: 100%;
    text-align: center;
    line-height: 1.1;
  }
  .winery__kind {
    font-size: 22px;
    font-weight: 500;
    letter-spacing: 3px;
    color: var(--green-light);
  }
  .winery__name {
    font-size: 46px;
    font-weight: 500;
    letter-spacing: 1px;
    color: var(--ink);
  }
  .bubble-field {
    position: absolute;
    left: 20px;
    top: 170px;
    width: 664px;
    height: 890px;
  }
  .product {
    position: absolute;
    top: 455px;
    left: 0;
    width: 100%;
    margin: 0;
    text-align: center;
    font-weight: 800;
    font-size: 92px;
    line-height: 87px;
    letter-spacing: -2px;
    color: var(--ink);
  }
  .volume {
    position: absolute;
    right: 40px;
    bottom: 30px;
    font-size: 30px;
    font-weight: 500;
    color: var(--ink);
  }
</style>
</head>
<body>
  <div class="label">
    <div class="winery">
      <div class="winery__kind">WEINGUT</div>
      <div class="winery__name">MARTIN BRAUER</div>
    </div>

    <svg class="bubble-field" viewBox="0 0 664 890" role="img" aria-label="Verstreutes Muster aus hell- und dunkelgrünen Perlen rund um den Produktnamen">
      <defs>
        <radialGradient id="bubble-glow" cx="50%" cy="50%" r="55%">
          <stop offset="0%" stop-color="#8fdc5a" stop-opacity="0.55"/>
          <stop offset="55%" stop-color="#6fd052" stop-opacity="0.35"/>
          <stop offset="100%" stop-color="#3fc24a" stop-opacity="0"/>
        </radialGradient>
      </defs>
      <rect width="664" height="890" fill="url(#bubble-glow)"/>
    </svg>

    <h1 class="product">TRAUBEN<br>SAFT<br>SCHORLE</h1>

    <div class="volume">0,33 l</div>
  </div>
</body>
</html>
```